Web Design Project for Karaoke Bar

This project is to redesign the clients current website. This is a karaoke bar in the Seattle downtown. Structure will remain the same. The "red-line" theme is a branded element along with the stick figure logo.
The would mostly like it updated to more modern looking site.
http://brambleloungekc.example/
We will want the contact information, including social media icons in the top right.
Social media integration of FB fan page is a must. Also a the map site map on the first page.
Target Market(s)
Mid 20's-30s, college students and professionals
Industry/Entity Type
Media
Look and feel

```html
<!DOCTYPE html>
<html lang="en">
<head>
<meta charset="utf-8">
<title>Bramble Lounge — Karaoke Bar</title>
<link rel="stylesheet" href="https://fonts.googleapis.com/css2?family=Questrial&family=Arimo:wght@400;700&family=Oswald:wght@500&family=Roboto+Slab:wght@800&display=swap">
<style>
:root{
  --night:#050505;
  --wine:#6a0f0f;
  --wine-deep:#3c0606;
  --neon:#ff2a2a;
  --panel:#ecebe8;
  --card:#ffffff;
  --ink:#222222;
  --muted:#555555;
  --nav:#f3a33a;
  --red-text:#c81414;
  --events:#f07c14;
  --happy:#159a8a;
  --new:#1c8fd6;
  --note:#fbe96a;
  --submit:#e8541a;
}
*{box-sizing:border-box;margin:0;padding:0}
html,body{width:1192px;height:1200px;overflow:hidden;background:var(--night)}
.stage{position:absolute;left:0;top:0;width:1000px;height:1007px;transform:scale(1.192);transform-origin:0 0;font-family:"Questrial",sans-serif;color:var(--ink)}
.abs{position:absolute}
.backdrop{left:0;top:0;width:1000px;height:1007px;background:
  radial-gradient(circle at 90px 300px,#8a8a8a 0,#3a3a3a 90px,transparent 200px),
  radial-gradient(circle at 910px 300px,#8a8a8a 0,#3a3a3a 90px,transparent 200px),
  linear-gradient(#1a1a1a,#000 60%)}
.site{left:224px;top:20px;width:606px;height:936px;background:linear-gradient(90deg,var(--wine-deep),var(--wine) 18%,#7a1212 50%,var(--wine) 82%,var(--wine-deep));border-radius:4px}
.neon-h{left:390px;top:86px;width:440px;height:2px;background:var(--neon);box-shadow:0 0 8px var(--neon)}
.neon-v{left:280px;top:140px;width:2px;height:816px;background:var(--neon);box-shadow:0 0 8px var(--neon)}
.brand{left:244px;top:62px;display:flex;align-items:center;gap:8px;color:#ffffff;font-size:18px;white-space:nowrap}
.brand-dot{width:40px;height:40px;border-radius:50%;background:#ffffff;flex:none}
.util{left:661px;top:34px;font-size:9px;color:#ffffff;display:flex;gap:6px}
.social{display:flex;gap:4px}
.social span{width:14px;height:14px;border-radius:2px;display:block}
.s1{background:#3b5ba0}.s2{background:#3fb5e6}.s3{background:#2b7bc0}.s4{background:#1d76b3}
.social-top{left:742px;top:31px}
.nav{left:467px;top:58px;display:flex;gap:0;font-size:10px;color:var(--nav);white-space:nowrap}
.nav a{color:inherit;text-decoration:none;padding:3px 11px;height:17px}
.nav a.active{background:#2a0606;border:1px solid #8b2a2a;border-radius:3px;color:#ffffff;padding:3px 8px}
.content{left:348px;top:116px;width:463px;height:743px;background:var(--panel);border-radius:3px}
.hero{left:354px;top:125px;width:451px;height:131px;background:linear-gradient(90deg,#33264a 0%,#5b3a78 35%,#c2508c 70%,#8b5fb8 100%);overflow:hidden}
.hero-title{left:367px;top:138px;font-family:"Oswald",sans-serif;font-size:30px;color:#f2a72e;letter-spacing:1px}
.hero-sub{left:367px;top:176px;font-size:14px;line-height:19px;color:#ffffff}
.hero-cta{left:367px;top:236px;font-family:"Arimo",sans-serif;font-weight:700;font-size:10px;color:#9ff04a}
.hero-arrow{top:231px;width:19px;height:18px;background:#111;border:1px solid #777}
.section-bar{left:354px;top:266px;width:450px;height:21px;background:linear-gradient(#fafafa,#d3d3d3);font-size:11px;padding:4px 6px;color:#333}
.about{left:354px;top:294px;width:290px;font-family:"Arimo",sans-serif}
.about h3{font-size:10px;font-weight:700}
.about .late{font-size:10px;font-weight:700;color:var(--red-text);margin-top:4px}
.about ul{list-style:none;margin-top:6px;font-size:9px;color:var(--muted)}
.about li{display:flex;gap:8px;align-items:center;height:21px;white-space:nowrap}
.about li svg{flex:none}
.photo{background:linear-gradient(135deg,#b33a3a,#e28a6a 50%,#5a4a55)}
.about-photo{left:660px;top:304px;width:135px;height:72px;border:3px solid #fff;box-shadow:0 0 3px #999}
.card{top:423px;width:142px;height:134px;background:var(--card);border-radius:4px;overflow:hidden}
.card-head{height:20px;color:#fff;font-size:11px;padding:4px 7px;white-space:nowrap}
.c-events{left:354px}.c-events .card-head{background:var(--events)}
.c-happy{left:508px}.c-happy .card-head{background:var(--happy)}
.c-new{left:662px}.c-new .card-head{background:var(--new)}
.events-art{margin:4px auto 0;width:90px;height:66px;background:linear-gradient(#e9e2cf,#9a9a9a)}
.events-cta{font-family:"Roboto Slab",serif;font-weight:800;font-size:13px;color:var(--red-text);text-align:center;line-height:17px;margin-top:2px}
.happy-list{list-style:none;font-family:"Arimo",sans-serif;font-size:7.8px;color:#333;padding:5px 6px 0 9px}
.happy-list li{height:13px;line-height:13px;display:flex;gap:5px;align-items:center;white-space:nowrap}
.happy-list li::before{content:"";flex:none;width:0;height:0;border-left:4px solid var(--happy);border-top:3px solid transparent;border-bottom:3px solid transparent}
.price{left:612px;top:417px;width:36px;height:36px;border-radius:50%;background:#d0141a;color:#fff;font-family:"Arimo",sans-serif;font-weight:700;font-size:10px;display:flex;align-items:center;justify-content:center;box-shadow:0 0 0 2px #f2f2f2}
.new-photo{margin:6px auto 0;width:124px;height:76px;border:2px solid #ddd;background:linear-gradient(135deg,#2a2a48,#7a5a3a 50%,#3a2a2a)}
.new-link{font-size:7px;color:var(--new);padding:5px 8px}
.label{font-family:"Arimo",sans-serif;font-weight:700;font-size:10px;color:#222}
.gallery{left:354px;top:590px;width:296px;height:80px;background:#fff;border-radius:3px}
.gal-arrow{top:610px;width:16px;height:36px;background:#e4e4e4;border-radius:8px}
.thumb{top:603px;width:58px;height:52px;border:3px solid #fff;box-shadow:0 0 3px #999}
.mail{left:663px;top:590px;width:140px;height:80px;background:#fff;border-radius:3px;padding:6px;font-family:"Arimo",sans-serif;font-size:8px;color:#444;line-height:13px}
.mail-field{left:670px;top:635px;width:89px;height:22px;background:#e6e6e6;font-size:7px;color:#777;padding:6px;white-space:nowrap}
.mail-btn{left:758px;top:635px;width:39px;height:22px;background:var(--submit);color:#fff;font-family:"Arimo",sans-serif;font-weight:700;font-size:7px;text-align:center;padding-top:7px}
.map{left:354px;top:706px;width:296px;height:147px;border:5px solid #c8c8c8;background:linear-gradient(135deg,#ebe7df,#d9d6cc 50%,#e8e2c6)}
.map-note{left:658px;top:704px;width:142px;text-align:center;font-family:"Arimo",sans-serif;font-weight:700;font-size:8px;line-height:13px;color:#7a1010}
.address{left:658px;top:756px;width:142px;text-align:center;font-family:"Arimo",sans-serif;font-weight:700;font-size:7.5px;color:#222}
.videos-title{left:348px;top:868px;font-family:"Arimo",sans-serif;font-weight:700;font-size:11px;color:#fff}
.video{top:892px;width:76px;height:44px;border:2px solid #4a0a0a;background:linear-gradient(135deg,#6b3a2a,#c79270 50%,#3a2a2a)}
.side-quiz{left:230px;top:253px;width:113px;height:117px;background:#fff;border:2px dashed #e8a33a}
.quiz-art{height:55px;background:linear-gradient(#c0392b,#e67e22)}
.quiz-text{font-family:"Arimo",sans-serif;font-weight:700;font-size:7.5px;line-height:12px;text-align:center;padding:3px 2px}
.side-badge{left:230px;top:388px;width:113px;height:75px;border:2px dashed #e8a33a;background:linear-gradient(#5a8fd0,#2a5aa0)}
.note{left:234px;top:490px;width:105px;height:132px;background:var(--note);transform:rotate(-1deg);font-family:"Arimo",sans-serif;font-size:8px;color:#222;padding:22px 4px 0;line-height:11px;box-shadow:1px 2px 4px rgba(0,0,0,.5);overflow:hidden}
.note b{font-size:11px;display:block;margin-bottom:9px}
.note .email{font-size:7.5px;white-space:nowrap}
.pin{left:281px;top:478px}
.footer{left:233px;top:966px;font-size:7px;color:#888;line-height:13px}
.social-foot{left:742px;top:970px}
</style>
</head>
<body>
<div class="stage">
  <div class="abs backdrop" role="img" aria-label="Concert crowd silhouettes under stage lights"></div>
  <div class="abs site"></div>
  <div class="abs neon-h"></div>
  <div class="abs neon-v"></div>

  <div class="abs brand"><span class="brand-dot"></span><span>Bramble Lounge</span></div>

  <div class="abs util"><span>Menu</span><span>/</span><span>Contact</span></div>
  <div class="abs social social-top"><span class="s1"></span><span class="s2"></span><span class="s3"></span><span class="s4"></span></div>

  <nav class="abs nav">
    <a class="active" href="#">Home</a><a href="#">Karaoke</a><a href="#">Sports</a><a href="#">Group Parties</a><a href="#">Pictures</a><a href="#">Bar</a>
  </nav>

  <div class="abs content"></div>

  <div class="abs hero" role="img" aria-label="Friends singing karaoke into a microphone"></div>
  <div class="abs hero-title">KARAOKE</div>
  <div class="abs hero-sub">Best Karaoke Bar In Town<br>7 years Running</div>
  <div class="abs hero-cta">NOW SING 7 DAYS A WEEK!</div>
  <div class="abs hero-arrow" style="left:754px"><svg width="17" height="16"><path d="M10 4 L6 8 L10 12" stroke="#fff" stroke-width="2" fill="none"/></svg></div>
  <div class="abs hero-arrow" style="left:777px"><svg width="17" height="16"><path d="M7 4 L11 8 L7 12" stroke="#fff" stroke-width="2" fill="none"/></svg></div>

  <div class="abs section-bar">Bramble Lounge</div>
  <div class="abs about">
    <h3>Bramble Lounge is open 7 days a week!</h3>
    <p class="late">Bat til 2AM !</p>
    <ul>
      <li><svg width="6" height="6"><path d="M0 0 L6 3 L0 6Z" fill="#6a9a3a"/></svg>Happy hour is Monday - Sunday 9:00 AM - 6:00 PM (Drinks Only)</li>
      <li><svg width="6" height="6"><path d="M0 0 L6 3 L0 6Z" fill="#6a9a3a"/></svg>Monday - Friday 3:00 PM - 6:00 PM (Food)</li>
      <li><svg width="6" height="6"><path d="M0 0 L6 3 L0 6Z" fill="#6a9a3a"/></svg>Happy hour ends at 5:30 PM During Arena Events.</li>
    </ul>
  </div>
  <div class="abs photo about-photo" role="img" aria-label="Group of friends at the bar"></div>

  <div class="abs card c-events">
    <div class="card-head">Events</div>
    <div class="events-art" role="img" aria-label="Microphone with flying cash"></div>
    <div class="events-cta">Singing for Cash<br>@ Bramble</div>
  </div>
  <div class="abs card c-happy">
    <div class="card-head">Happy Hour Menu</div>
    <ul class="happy-list">
      <li>MON thru 11am - 7pm</li><li>Chicken Strips &amp; Fries</li><li>Fish &amp; Fries</li><li>Sliders &amp; Fries</li><li>Wings &amp; Fries</li><li>Pot Stickers</li><li>Bacon &amp; Cheese Fries or Tots</li><li>Pepperoni Pizza</li>
    </ul>
  </div>
  <div class="abs price">$3.99</div>
  <div class="abs card c-new">
    <div class="card-head">New @ Bramble</div>
    <div class="new-photo" role="img" aria-label="Crowded bar room from above"></div>
    <div class="new-link">CLICK HERE TO VIEW ⊙</div>
  </div>

  <div class="abs label" style="left:354px;top:574px">Photo Gallery</div>
  <div class="abs gallery"></div>
  <div class="abs gal-arrow" style="left:358px"></div>
  <div class="abs gal-arrow" style="left:630px"></div>
  <div class="abs thumb photo" style="left:388px" role="img" aria-label="Guests posing in hats"></div>
  <div class="abs thumb photo" style="left:473px" role="img" aria-label="Guests dancing"></div>
  <div class="abs thumb photo" style="left:557px" role="img" aria-label="Bartender at the counter"></div>

  <div class="abs label" style="left:663px;top:574px">Join Our Mailing List</div>
  <div class="abs mail">List of receive update, event details, &amp; prize giveaways!</div>
  <div class="abs mail-field">Enter email address</div>
  <div class="abs mail-btn">SUBMIT</div>

  <div class="abs label" style="left:354px;top:690px">Map to Bramble Lounge</div>
  <div class="abs map" role="img" aria-label="Street map showing the bar location"></div>
  <div class="abs map-note">You can click on the map below to go to the map site to get driving directions to Bramble Lounge</div>
  <div class="abs address">214 W. Bramble Ave. Kansas City, MO 64105</div>

  <div class="abs videos-title">Watch Our Videos</div>
  <div class="abs video" style="left:362px" role="img" aria-label="Video still of guests"></div>
  <div class="abs video" style="left:481px" role="img" aria-label="Video still of singer"></div>
  <div class="abs video" style="left:600px" role="img" aria-label="Video still of pool table"></div>
  <div class="abs video" style="left:719px" role="img" aria-label="Video still of crowd"></div>

  <div class="abs side-quiz">
    <div class="quiz-art" role="img" aria-label="Cartoon quiz night banner"></div>
    <div class="quiz-text">Brainy Pint Pub Quiz: Wednesdays @ 7pm. Free to play. Win bar cash &amp; Internet Fame</div>
  </div>
  <div class="abs side-badge" role="img" aria-label="Local news feature badge"></div>

  <div class="abs note">
    You can Contact us at<b>816.555.0142</b>
    To make a Reservation<b>816.555.0177</b>
    e-mail at<br><span class="email">hello@bramblekc.example</span>
  </div>
  <svg class="abs pin" width="22" height="24"><circle cx="13" cy="8" r="6" fill="#e0a020"/><path d="M10 12 L3 22" stroke="#888" stroke-width="2"/></svg>

  <div class="abs footer">Copyright © 2012 Bramble Lounge. All Rights Reserved.<br>Home / Karaoke / Sports / Group Parties / Pictures / Bar</div>
  <div class="abs social social-foot"><span class="s1"></span><span class="s2"></span><span class="s3"></span><span class="s4"></span></div>
</div>
</body>
</html>
```